We need a very creative business card for a leading diamond tools manufactures in india

1. Iso 9001:2000
2. Logo
3. Leading Manufacture of stone cutting tools: Gang Saw Segment, Circular Segment, wire saw segment and rubber and plastic coated diamond wire rope.
4. Spirit for success
5. Kalvani Mokesh Diamond Tools Pvt. Ltd.
6. Mo. No. 9817406352
7. Email: Rakesh@kmgroup-tardex.com
8. Web: kmgroup-tardex.com
9.CEO
10. Reg. Office. 47, pushpa vihar , naya basti, dholpura ,dist. Rajsamand (rajasthan) 313587
11.Rakesh Jandal
Our audience are Adult based in english speaking person having age between 25-55 that handle granite and marble business.
Plastic

```html
<!DOCTYPE html>
<html lang="en">
<head>
<meta charset="utf-8">
<title>Kalvani Mokesh Diamond Tools Business Card</title>
<link rel="stylesheet" href="https://fonts.googleapis.com/css2?family=Montserrat:wght@400;500;600&display=swap">
<style>
  :root {
    --bg: #8c8c8c;
    --card: #ffffff;
    --orange: #f2a11d;
    --yellow: #f5c518;
    --icon: #e8482b;
    --ink: #3b3b3b;
    --muted: #6a6a6a;
    --brand: #d9951a;
  }
  * { margin: 0; padding: 0; box-sizing: border-box; }
  html, body { width: 1200px; height: 988px; overflow: hidden; }
  body {
    background: var(--bg);
    font-family: "Montserrat", sans-serif;
    position: relative;
  }
  .card {
    position: absolute;
    width: 540px;
    height: 310px;
    background: var(--card);
    border-top: 12px solid var(--orange);
    box-shadow: 0 12px 30px rgba(0,0,0,0.35);
  }
  .card--back { left: 50px; top: 150px; }
  .card--front { left: 610px; top: 520px; }

  .brand {
    display: flex;
    align-items: center;
    justify-content: center;
    gap: 10px;
    color: var(--brand);
    font-weight: 600;
    white-space: nowrap;
  }
  .brand__dot {
    width: 16px; height: 16px;
    border-radius: 50%;
    background: var(--brand);
    flex: none;
  }

  /* Back */
  .card--back .brand {
    position: absolute; left: 0; right: 0; top: 96px;
    font-size: 19px;
  }
  .card--back .brand__dot { width: 22px; height: 22px; }
  .tagline {
    position: absolute; left: 0; right: 0; top: 132px;
    text-align: center;
    font-size: 11px; letter-spacing: 3px; text-transform: uppercase;
    color: var(--muted);
  }
  .products {
    position: absolute; left: 40px; right: 40px; top: 210px;
    text-align: center;
    font-size: 9.5px; line-height: 1.5;
    color: var(--muted);
  }
  .cert {
    position: absolute; left: 0; right: 0; top: 262px;
    text-align: center;
    font-size: 10px; font-weight: 600; letter-spacing: 1px;
    color: var(--ink);
  }

  /* Front */
  .card--front .brand {
    position: absolute; left: 0; right: 0; top: 44px;
    font-size: 16px;
  }
  .rule {
    position: absolute; left: 0; right: 0;
    height: 3px; background: var(--yellow);
  }
  .rule--upper { top: 112px; }
  .rule--lower { top: 262px; }

  .contacts {
    position: absolute;
    left: 228px; top: 126px; right: 14px;
    display: grid;
    grid-template-columns: 1fr 1fr;
    row-gap: 7px;
    column-gap: 8px;
    font-size: 10px;
    color: var(--muted);
  }
  .contacts__item { display: flex; align-items: center; gap: 6px; white-space: nowrap; }
  .contacts__item--wide { grid-column: 1 / 3; }
  .contacts__item--wrap { white-space: normal; align-items: flex-start; line-height: 1.4; }
  .contacts__icon { width: 14px; height: 14px; flex: none; }

  .holder {
    position: absolute;
    left: 22px; top: 214px;
  }
  .holder__name {
    font-size: 15px; font-weight: 500; letter-spacing: 1px;
    color: var(--ink); text-transform: uppercase;
  }
  .holder__role {
    font-size: 9px; letter-spacing: 1px; color: var(--muted);
    text-transform: uppercase; margin-top: 3px;
  }
</style>
</head>
<body>
  <section class="card card--back" aria-label="Card back">
    <div class="brand"><span class="brand__dot"></span>Kalvani Mokesh Diamond Tools Pvt. Ltd.</div>
    <p class="tagline">Spirit for Success</p>
    <p class="products">Leading Manufacturer of Stone Cutting Tools: Gang Saw Segment, Circular Segment, Wire Saw Segment and Rubber &amp; Plastic Coated Diamond Wire Rope</p>
    <p class="cert">ISO 9001:2000</p>
  </section>

  <section class="card card--front" aria-label="Card front">
    <div class="brand"><span class="brand__dot"></span>Kalvani Mokesh Diamond Tools Pvt. Ltd.</div>
    <div class="rule rule--upper"></div>

    <div class="contacts">
      <div class="contacts__item">
        <svg class="contacts__icon" viewBox="0 0 14 14"><circle cx="7" cy="7" r="7" fill="var(--icon)"/><path d="M4.5 3.8l1.3-.3.8 1.8-.9.7a5 5 0 0 0 2.3 2.3l.7-.9 1.8.8-.3 1.3c-3 .3-6-2.7-5.7-5.7z" fill="#fff"/></svg>
        Mo. 9817406352
      </div>
      <div class="contacts__item">
        <svg class="contacts__icon" viewBox="0 0 14 14"><circle cx="7" cy="7" r="7" fill="var(--icon)"/><circle cx="7" cy="7" r="3.5" fill="none" stroke="#fff" stroke-width="1"/><path d="M3.5 7h7M7 3.5v7" stroke="#fff" stroke-width="0.8"/></svg>
        kmgroup-tardex.com
      </div>
      <div class="contacts__item contacts__item--wide">
        <svg class="contacts__icon" viewBox="0 0 14 14"><circle cx="7" cy="7" r="7" fill="var(--icon)"/><rect x="3.5" y="4.5" width="7" height="5" fill="none" stroke="#fff" stroke-width="1"/><path d="M3.5 4.5L7 7.5l3.5-3" fill="none" stroke="#fff" stroke-width="1"/></svg>
        Rakesh@kmgroup-tardex.com
      </div>
      <div class="contacts__item contacts__item--wide contacts__item--wrap">
        <svg class="contacts__icon" viewBox="0 0 14 14"><circle cx="7" cy="7" r="7" fill="var(--icon)"/><path d="M7 11S4.3 7.9 4.3 6a2.7 2.7 0 0 1 5.4 0C9.7 7.9 7 11 7 11z" fill="#fff"/><circle cx="7" cy="6" r="1" fill="var(--icon)"/></svg>
        <span>Reg. Office: 47, pushpa vihar, naya basti, dholpura, dist. Rajsamand (rajasthan) 313587</span>
      </div>
    </div>

    <div class="holder">
      <p class="holder__name">Rakesh Jandal</p>
      <p class="holder__role">CEO</p>
    </div>
    <div class="rule rule--lower"></div>
  </section>
</body>
</html>
```